Bag Design For Outdoors Industry

We are a Midwest seed company that is looking for a bag design for our Food Plot Product Line, "Ridgehorn". We are looking for a broad design that will work for several SKUs. Attached is the dieline for 4.5"x9.5"x20.75" bag and specifications for the print company. Also included are the brand standards and our catalog. The bag design should pull the themes and concepts established in the catalog. We will be placing 4"x9" labels on the front and back of the bag (design should have a guide for labels). Front of package will include a clear window to see the product. Use the attached layout PDF for a rough idea of how it should be formatted. The final design should convey the simple brand and overall themes.

Target Market(s)

Outdoor enthusiasts

Industry/Entity Type

Outdoors

Requirements
Must have
• Follow our provided branding, clear window

```html
<!DOCTYPE html>
<html lang="en">
<head>
<meta charset="utf-8">
<title>Ridgehorn Food Plot Seed – Bag Dieline</title>
<link href="https://fonts.googleapis.com/css2?family=Montserrat:wght@400;800&family=Open+Sans:wght@400&family=Russo+One&display=swap" rel="stylesheet">
<style>
  :root {
    --ink: #000000;
    --paper: #ffffff;
    --brand-orange: #f0a500;
    --cliff-orange: #ee9a06;
    --window-grey: #383838;
    --guide-grey: #8a8a8a;
    --dieline-red: #e30613;
    --ridge-1: #222222;
    --ridge-2: #444444;
    --ridge-3: #5e5e5e;
    --ridge-4: #777777;
  }
  html, body {
    margin: 0;
    padding: 0;
    width: 1200px;
    height: 867px;
    overflow: hidden;
    background: var(--paper);
  }
  .bag-flat {
    position: relative;
    width: 1200px;
    height: 867px;
    overflow: hidden;
  }
  .print-area {
    position: absolute;
    left: 8px;
    top: 6px;
    width: 1182px;
    height: 854px;
    background: var(--ink);
    overflow: hidden;
  }
  .ridge-scene {
    position: absolute;
    left: 0;
    top: 470px;
    width: 1182px;
    height: 384px;
    background: linear-gradient(to bottom,
      var(--ink) 0%,
      var(--ridge-1) 12%,
      var(--ridge-2) 32%,
      var(--ridge-3) 60%,
      var(--ridge-4) 100%);
  }
  .buck-on-cliff {
    position: absolute;
    left: 408px;
    top: 508px;
    width: 182px;
    height: 346px;
    background: linear-gradient(to bottom, var(--brand-orange), var(--cliff-orange));
  }
  .brand-square {
    position: absolute;
    left: 346px;
    top: 66px;
    width: 97px;
    height: 97px;
    background: var(--brand-orange);
  }
  .wordmark {
    position: absolute;
    left: 253px;
    top: 216px;
    width: 282px;
    font-family: "Montserrat", sans-serif;
    color: var(--paper);
    text-align: right;
  }
  .wordmark-name {
    display: block;
    font-weight: 800;
    font-size: 38px;
    line-height: 38px;
    letter-spacing: -0.5px;
    text-align: center;
  }
  .wordmark-tag {
    display: block;
    font-weight: 400;
    font-size: 8.5px;
    letter-spacing: 1.6px;
    line-height: 10px;
  }
  .side-mark {
    position: absolute;
    top: 260px;
    width: 380px;
    height: 60px;
    transform-origin: 0 0;
    transform: rotate(-90deg);
    font-family: "Montserrat", sans-serif;
    color: var(--paper);
  }
  .side-mark.left { left: 82px; top: 626px; }
  .side-mark.right { left: 672px; top: 626px; }
  .side-mark-name {
    position: absolute;
    left: 0;
    top: 0;
    font-weight: 800;
    font-size: 46px;
    line-height: 46px;
    letter-spacing: 0.5px;
  }
  .side-mark-tag {
    position: absolute;
    left: 0;
    top: 48px;
    font-weight: 400;
    font-size: 11px;
    letter-spacing: 1.6px;
    line-height: 12px;
    width: 364px;
    text-align: right;
  }
  .label-guide {
    position: absolute;
    box-sizing: border-box;
    display: flex;
    align-items: center;
    justify-content: center;
    font-family: "Open Sans", sans-serif;
    font-size: 16px;
    color: var(--guide-grey);
  }
  .label-guide.front {
    left: 206px;
    top: 274px;
    width: 378px;
    height: 167px;
    border: 1px dashed #444444;
    padding-bottom: 18px;
  }
  .label-guide.back {
    left: 795px;
    top: 639px;
    width: 379px;
    height: 167px;
    border: 1px dashed var(--dieline-red);
    color: #c8c8c8;
    padding-bottom: 12px;
  }
  .clear-window {
    position: absolute;
    left: 0;
    top: 0;
  }
  .clear-window-label {
    position: absolute;
    left: 225px;
    top: 798px;
    font-family: "Open Sans", sans-serif;
    font-size: 12px;
    letter-spacing: 0.3px;
    color: var(--guide-grey);
  }
  .taglines {
    position: absolute;
    left: 786px;
    top: 90px;
    width: 412px;
    margin: 0;
    padding: 0;
    list-style: none;
    text-align: center;
    font-family: "Russo One", sans-serif;
    font-size: 15px;
    letter-spacing: 2.6px;
    color: var(--brand-orange);
  }
  .taglines li { height: 35px; line-height: 30px; }
  .dieline {
    position: absolute;
    left: 0;
    top: 0;
    pointer-events: none;
  }
</style>
</head>
<body>
<main class="bag-flat">
  <div class="print-area">
    <div class="ridge-scene" role="img" aria-label="Layered grey mountain ridges fading into the night sky across every panel"></div>
    <div class="buck-on-cliff" role="img" aria-label="Orange illustration of a whitetail buck standing on a rocky cliff edge"></div>
  </div>

  <div class="brand-square" aria-hidden="true"></div>
  <div class="wordmark">
    <span class="wordmark-name">RIDGEHORN</span>
    <span class="wordmark-tag">FOOD PLOT SEED</span>
  </div>

  <div class="label-guide front">GUIDE FOR 4x9 Label</div>

  <svg class="clear-window" width="1200" height="867" viewBox="0 0 1200 867" aria-label="Clear window">
    <polygon points="219,675 219,848 565,848" fill="var(--window-grey)" stroke="#000" stroke-width="1.2"/>
  </svg>
  <span class="clear-window-label">CLEAR WINDOW</span>

  <div class="side-mark left">
    <span class="side-mark-name">RIDGEHORN</span>
    <span class="side-mark-tag">FOOD PLOT SEED</span>
  </div>
  <div class="side-mark right">
    <span class="side-mark-name">RIDGEHORN</span>
    <span class="side-mark-tag">FOOD PLOT SEED</span>
  </div>

  <ul class="taglines">
    <li>SOURCED PURE.</li>
    <li>PACKAGED FRESH.</li>
    <li>SIMPLE BRAND.</li>
  </ul>

  <div class="label-guide back">GUIDE FOR 4x9 Label</div>

  <svg class="dieline" width="1200" height="867" viewBox="0 0 1200 867" aria-hidden="true">
    <g stroke="var(--dieline-red)" stroke-width="0.8" fill="none">
      <rect x="8" y="6" width="1182" height="854"/>
      <line x1="205" y1="6" x2="205" y2="860"/>
      <line x1="598" y1="6" x2="598" y2="860"/>
      <line x1="794" y1="6" x2="794" y2="860"/>
    </g>
  </svg>
</main>
</body>
</html>
```